Ink & Toner Sales Flyer

2 Sided.
Ink & Toner Flyer
Front:
Header:
Are you one of the millions who have often complained about the high prices of ink and toner replacement cartridges?
Sub Header:
Well, now you will be able to take advantage of significant discounted pricing on all major brand replacement products through Korvel Supply.
Tagline: High Quality ink and toner at the lowest prices in the market today!

You can view our line of ink & toner and pharmacy vial products on www.korvelsupply.example.

ORDER ONLINE korvelsupply.example
ORDER BY PHONE 877-414-2596
ORDER BY FAX 866-305-4182
Backside:
Highest Quality Standards Utilized and Save Up to 70% off Retail
Did you know we manufacture brand new parts and build to the highest performance and quality standards (ISO-9001). We are a direct Manufacturer.
We replace the important mechanisms with brand new components to ensure that quality and performance is up to our standards, and yours. This is not a “Drill and Fill’ that you will find in the market.
We have been producing quality products for over 30 years. We have focused on businesses that need their products at peak performance for their business.

Wide Selection for Tavrin, Quolby, ZR, Bendrook and Felquist are excellent choices.
High Print Quality, Page Yield and Longevity.

Product Guarantee
We are confident in our products’ performance and yield; we offer a 100% product replacement guarantee for 60 days from the date of purchase.
Pricing Guarantee
In the unlikely event you find a comparable product at a lower cost, we guarantee to lower our price to beat that price and reward you with a 10% discount on your next order for bringing it to our attention.
Printer Warranty
Using our Compatible Remanufactured Cartridges will not void the manufacturer’s warranty.
Savings:

OEM Quality Toner
(Savings Comparison on Attachment for Prices.)

ORDER BY FAX 866-305-4182

Please call 877-414-2596 for Special Product Orders, Vials and Toner Bundle Pricing, Vial Samples & Any Other Additional Information.

Requirements
Must have
• Logo, Pricing Comparison in Any Format

```html
<!DOCTYPE html>
<html lang="en">
<head>
<meta charset="utf-8">
<title>Korvel Supply – Ink &amp; Toner Flyer</title>
<link href="https://fonts.googleapis.com/css2?family=Oswald:wght@400;500;600&family=Tinos:wght@400;700&family=Open+Sans:wght@400;600&display=swap" rel="stylesheet">
<style>
:root{
  --bg:#e9e9f6;
  --blue:#1b77c8;
  --blue-dark:#0f5ea8;
  --orange:#f7931e;
  --ink:#1d1d1d;
  --grey:#d9dadc;
  --grey-light:#f1f1f2;
  --white:#ffffff;
  --photo-a:#c9ccd3;
  --photo-b:#f4f4f6;
}
*{margin:0;padding:0;box-sizing:border-box}
html,body{width:825px;height:1200px;overflow:hidden;background:var(--bg)}
body{position:relative;font-family:"Tinos",serif;color:var(--ink)}
.page{position:absolute;background:var(--white);overflow:hidden;box-shadow:0 1px 3px rgba(0,0,0,.15)}
.abs{position:absolute}

/* ---------- front ---------- */
.front{width:348px;height:445px}
.front--top{left:77px;top:65px}
.front--large{left:197px;top:610px;transform:scale(1.24);transform-origin:0 0}
.front__headline{left:0;top:0;width:118px;height:225px;background:var(--blue);color:var(--white);
  font-family:"Oswald",sans-serif;font-weight:500;text-transform:uppercase;text-align:center;padding:26px 4px 0;line-height:1.2}
.front__headline span{display:block;white-space:nowrap}
.hl-s{font-size:11.5px}.hl-m{font-size:13.5px}.hl-l{font-size:17px}
.front__photo{left:118px;top:0;width:230px;height:225px;background:linear-gradient(160deg,var(--photo-b) 30%,var(--photo-a))}
.logo{display:flex;align-items:center;gap:4px;font-family:"Oswald",sans-serif;font-weight:500;color:var(--blue-dark);font-size:8px;white-space:nowrap}
.logo__dot{width:9px;height:9px;border-radius:50%;background:var(--blue)}
.front__logo{right:10px;top:30px}
.front__rule{left:0;top:225px;width:348px;height:4px;background:var(--blue)}
.front__sub{left:10px;top:229px;width:108px;height:201px;background:var(--orange);color:var(--white);
  font-family:"Oswald",sans-serif;font-weight:500;font-size:11px;line-height:1.5;text-transform:uppercase;text-align:center;padding:14px 2px 0}
.front__sub span{display:block;white-space:nowrap}
.front__tagline{left:125px;top:236px;width:188px;height:44px;background:var(--grey-light);border-bottom:2px solid var(--grey);
  font-family:"Oswald",sans-serif;font-weight:500;font-size:10.5px;line-height:1.3;text-align:center;color:#333;text-transform:uppercase;padding:6px 4px}
.front__note{left:125px;top:288px;width:188px;font-size:5.6px;text-align:center}
.front__url{left:125px;top:296px;width:188px;text-align:center;color:var(--blue);font-size:8.5px}
.order{left:125px;width:188px;height:28px;background:linear-gradient(var(--grey-light),var(--grey));display:flex;align-items:center}
.order svg{width:26px;height:20px;margin-left:8px}
.order__text{flex:1;text-align:center;font-size:8px;text-transform:uppercase;line-height:1.15}
.order__text b{display:block;font-weight:400;color:var(--blue);text-transform:none}
.order--1{top:318px}.order--2{top:350px}.order--3{top:382px}
.front__edge{left:313px;top:312px;width:4px;height:118px;background:var(--blue)}
.front__printer{left:264px;top:410px;width:32px;height:20px;background:linear-gradient(#9a9ea4,#55595e);border-radius:3px}
.front__band{left:0;top:430px;width:348px;height:15px}

/* ---------- back ---------- */
.back{left:437px;top:65px;width:320px;height:445px}
.back__head{left:0;top:0;width:320px;height:118px;background:var(--blue);color:var(--white);padding:7px 10px 0}
.back__title{font-family:"Oswald",sans-serif;font-weight:500;font-size:10.5px;text-transform:uppercase;margin-bottom:5px;white-space:nowrap}
.back__intro{font-size:7.2px;line-height:1.38}
.back__notch{left:296px;top:117px}
.guarantee{left:8px;width:158px;border-left:3px solid var(--orange);padding-left:6px}
.guarantee h3{font-family:"Oswald",sans-serif;font-weight:500;font-size:9px;text-transform:uppercase;margin-bottom:2px}
.guarantee p{font-size:7.2px;line-height:1.37}
.guarantee--1{top:128px}.guarantee--2{top:188px}.guarantee--3{top:263px}
.guarantee--2{border-color:var(--blue)}
.back__selection{left:172px;top:128px;width:140px;height:72px;background:linear-gradient(var(--white),var(--grey));
  font-size:7.4px;line-height:1.38;text-align:center;padding:8px 6px;box-shadow:0 2px 3px rgba(0,0,0,.18)}
.savings{left:172px;top:218px;width:143px}
.savings__head{display:flex;justify-content:space-between;align-items:baseline;border-bottom:1.5px solid var(--blue);padding-bottom:1px}
.savings__title{font-family:"Oswald",sans-serif;font-weight:500;color:var(--blue);font-size:9.5px;text-transform:uppercase}
.savings__sub{color:var(--blue);font-size:7.5px}
.savings table{width:100%;border-collapse:collapse;font-family:"Open Sans",sans-serif;font-size:4.6px;margin-top:2px}
.savings th{background:#1d1d1d;color:var(--white);font-weight:600;padding:1px 2px;text-align:left;white-space:nowrap}
.savings td{padding:2.4px 2px;border-bottom:.5px solid #bbb;white-space:nowrap}
.savings td+td{border-left:.5px solid #bbb}
.back__foot{left:0;top:345px;width:320px;height:100px;background:var(--orange)}
.back__order{left:8px;top:354px;width:168px}
.back__order-note{font-size:5.2px;margin-bottom:6px}
.back__order-row{display:flex;justify-content:space-between;align-items:baseline;font-size:7.6px;text-transform:uppercase;margin-bottom:5px;white-space:nowrap}
.back__order-row b{font-weight:400;font-size:8.6px;letter-spacing:.3px;text-transform:none}
.back__divider{left:180px;top:345px;width:1px;height:100px;background:rgba(255,255,255,.6)}
.back__call{left:186px;top:354px;width:128px;font-size:7px;line-height:1.35;font-weight:400}
.back__logo{right:10px;top:425px;font-size:6px}
</style>
</head>
<body>

<section class="page front front--top">
  <h1 class="abs front__headline">
    <span class="hl-s">Are you one of</span>
    <span class="hl-l">The millions</span>
    <span class="hl-s">who have often</span>
    <span class="hl-l">Complained</span>
    <span class="hl-s">about the high</span>
    <span class="hl-m">prices of ink &amp;</span>
    <span class="hl-s">toner replacement</span>
    <span class="hl-l">Cartridges?</span>
  </h1>
  <div class="abs front__photo" role="img" aria-label="Two office workers reviewing papers beside a stack of colour toner cartridges"></div>
  <div class="abs logo front__logo"><span class="logo__dot"></span>Korvel Supply, LLC.</div>
  <div class="abs front__rule"></div>
  <p class="abs front__sub"><span>Well, now you will</span><span>be able to take</span><span>advantage of</span><span>significant dis-</span><span>counted pricing on</span><span>all major brand</span><span>replacement</span><span>products through</span><span>Korvel Supply.</span></p>
  <p class="abs front__tagline">High quality ink and toner at the lowest prices in the market today!</p>
  <p class="abs front__note">You can view our line of ink &amp; toner and pharmacy vial products on</p>
  <p class="abs front__url">www.korvelsupply.example.</p>
  <div class="abs order order--1"><svg viewBox="0 0 26 20"><path d="M3 11 L10 17 L24 2" fill="none" stroke="#f7931e" stroke-width="3.5" stroke-linecap="round" stroke-linejoin="round"/></svg><p class="order__text">Order online<b>korvelsupply.example</b></p></div>
  <div class="abs order order--2"><svg viewBox="0 0 26 20"><path d="M3 11 L10 17 L24 2" fill="none" stroke="#f7931e" stroke-width="3.5" stroke-linecap="round" stroke-linejoin="round"/></svg><p class="order__text">Order by phone<b>877-414-2596</b></p></div>
  <div class="abs order order--3"><svg viewBox="0 0 26 20"><path d="M3 11 L10 17 L24 2" fill="none" stroke="#f7931e" stroke-width="3.5" stroke-linecap="round" stroke-linejoin="round"/></svg><p class="order__text">Order by fax<b>866-305-4182</b></p></div>
  <div class="abs front__edge"></div>
  <div class="abs front__printer" role="img" aria-label="Small office printer"></div>
  <svg class="abs front__band" viewBox="0 0 348 15" preserveAspectRatio="none"><rect width="348" height="15" fill="#1b77c8"/><path d="M0 0 H348 V4 Q200 14 0 6Z" fill="#fff"/><path d="M120 15 Q240 4 348 8 V15Z" fill="#0f5ea8"/></svg>
</section>

<section class="page back">
  <div class="abs back__head">
    <h2 class="back__title">Highest quality standards utilized and save up to 70% off retail</h2>
    <p class="back__intro">Did you know we manufacture brand new parts and build to the highest performance and quality standards (ISO-9001). We are a direct Manufacturer. We replace the important mechanisms with brand new components to ensure that quality and performance is up to our standards, and yours. This is not a “Drill and Fill” that you will find in the market. We have been producing quality products for over 30 years. We have focused on businesses that need their products at peak performance for their business.</p>
  </div>
  <svg class="abs back__notch" width="14" height="8" viewBox="0 0 14 8"><path d="M0 0 H14 L7 8Z" fill="#1b77c8"/></svg>
  <div class="abs guarantee guarantee--1"><h3>Product guarantee</h3><p>We are confident in our products’ performance and yield; we offer a 100% product replacement guarantee for 60 days from the date of purchase.</p></div>
  <div class="abs guarantee guarantee--2"><h3>Pricing guarantee</h3><p>In the unlikely event you find a comparable product at a lower cost, we guarantee to lower our price to beat that price and reward you with a 10% discount on your next order for bringing it to our attention.</p></div>
  <div class="abs guarantee guarantee--3"><h3>Printer warranty</h3><p>Using our Compatible Remanufactured Cartridges will not void the manufacturer’s warranty.</p></div>
  <p class="abs back__selection">Wide Selection for Tavrin, Quolby, ZR, Bendrook and Felquist are excellent choices.<br>High Print Quality, Page Yield and Longevity.</p>
  <div class="abs savings">
    <div class="savings__head"><span class="savings__title">Savings</span><span class="savings__sub">OEM Quality Toner</span></div>
    <table>
      <tr><th>Printer</th><th>OEM Price</th><th>Korvel Price</th><th>% Savings</th></tr>
      <tr><td>Bendrook K410</td><td>$221.99</td><td>$169.99</td><td>23%</td></tr>
      <tr><td>Bendrook K42x</td><td>$393.99</td><td>$203.94</td><td>48%</td></tr>
      <tr><td>Bendrook K44x</td><td>$212.00</td><td>$160.00</td><td>25%</td></tr>
      <tr><td>Bendrook K46X</td><td>$271.99</td><td>$239.94</td><td>12%</td></tr>
      <tr><td>Hallard QR520</td><td>$ 68.49</td><td>$ 46.00</td><td>33%</td></tr>
      <tr><td>Hallard QR 530</td><td>$ 65.49</td><td>$ 37.00</td><td>44%</td></tr>
      <tr><td>ZR PageJet 2200</td><td>$152.99</td><td>$125.99</td><td>18%</td></tr>
    </table>
  </div>
  <div class="abs back__foot"></div>
  <div class="abs back__order">
    <p class="back__order-note">You can view our line of ink &amp; toner and pharmacy vial products on www.korvelsupply.example.</p>
    <p class="back__order-row">Order online <b>korvelsupply.example</b></p>
    <p class="back__order-row">Order by phone <b>877-414-2596</b></p>
    <p class="back__order-row">Order by fax <b>866-305-4182</b></p>
  </div>
  <div class="abs back__divider"></div>
  <p class="abs back__call">Please call 877-414-2596 for Special Product Orders, Vials and Toner Bundle Pricing, Vial Samples &amp; Any Other Additional Information.</p>
  <div class="abs logo back__logo"><span class="logo__dot"></span>Korvel Supply, LLC</div>
</section>

<section class="page front front--large" aria-hidden="true">
  <div class="abs front__headline">
    <span class="hl-s">Are you one of</span>
    <span class="hl-l">The millions</span>
    <span class="hl-s">who have often</span>
    <span class="hl-l">Complained</span>
    <span class="hl-s">about the high</span>
    <span class="hl-m">prices of ink &amp;</span>
    <span class="hl-s">toner replacement</span>
    <span class="hl-l">Cartridges?</span>
  </div>
  <div class="abs front__photo"></div>
  <div class="abs logo front__logo"><span class="logo__dot"></span>Korvel Supply, LLC.</div>
  <div class="abs front__rule"></div>
  <p class="abs front__sub"><span>Well, now you will</span><span>be able to take</span><span>advantage of</span><span>significant dis-</span><span>counted pricing on</span><span>all major brand</span><span>replacement</span><span>products through</span><span>Korvel Supply.</span></p>
  <p class="abs front__tagline">High quality ink and toner at the lowest prices in the market today!</p>
  <p class="abs front__note">You can view our line of ink &amp; toner and pharmacy vial products on</p>
  <p class="abs front__url">www.korvelsupply.example.</p>
  <div class="abs order order--1"><svg viewBox="0 0 26 20"><path d="M3 11 L10 17 L24 2" fill="none" stroke="#f7931e" stroke-width="3.5" stroke-linecap="round" stroke-linejoin="round"/></svg><p class="order__text">Order online<b>korvelsupply.example</b></p></div>
  <div class="abs order order--2"><svg viewBox="0 0 26 20"><path d="M3 11 L10 17 L24 2" fill="none" stroke="#f7931e" stroke-width="3.5" stroke-linecap="round" stroke-linejoin="round"/></svg><p class="order__text">Order by phone<b>877-414-2596</b></p></div>
  <div class="abs order order--3"><svg viewBox="0 0 26 20"><path d="M3 11 L10 17 L24 2" fill="none" stroke="#f7931e" stroke-width="3.5" stroke-linecap="round" stroke-linejoin="round"/></svg><p class="order__text">Order by fax<b>866-305-4182</b></p></div>
  <div class="abs front__edge"></div>
  <div class="abs front__printer"></div>
  <svg class="abs front__band" viewBox="0 0 348 15" preserveAspectRatio="none"><rect width="348" height="15" fill="#1b77c8"/><path d="M0 0 H348 V4 Q200 14 0 6Z" fill="#fff"/><path d="M120 15 Q240 4 348 8 V15Z" fill="#0f5ea8"/></svg>
</section>

</body>
</html>
```